Small Box Design - For launch into retail market

We need artwork for small boxes that we are going to be using for the retail market. I will upload the type of box we are going to be using. The example we are uploading is of a different company that sells the same products. We would like our Logo on the box as as our web address (www.brandellgroup-ltd.com). The rest is up to you. Please contact with any questions.

Target Market(s)

Distributors, Retailers of Fasteners

Industry/Entity Type

Manufacture

Colors
0355a3
3176b5
fbee3f
fbf289

Requirements
Must have
• Our logo, our web address www.brandellgroup-ltd.com
• Somewhere on the box Washers . Stampings . Assemblies . Bearings (most likely below our logo somewhere)
Nice to have
• Blue is our corporate colour, but it's not essential. You can suggest any colours and we will consider.

```html
<!DOCTYPE html>
<html lang="en">
<head>
<meta charset="utf-8">
<title>Brandell Limited – Retail Box Dieline</title>
<link href="https://fonts.googleapis.com/css2?family=Roboto+Condensed:wght@400;700&display=swap" rel="stylesheet">
<style>
  :root{
    --blue:#0355a3;
    --blue-mid:#1a5fb4;
    --blue-light:#3176b5;
    --logo-blue:#1f3fae;
    --yellow:#fbee3f;
    --cream:#fbf289;
    --gold:#e6a53a;
    --steel-a:#c9ccd0;
    --steel-b:#7d8289;
    --white:#ffffff;
  }
  html,body{margin:0;padding:0;width:1200px;height:1200px;overflow:hidden;background:var(--white);}
  .canvas{position:relative;width:1200px;height:1200px;font-family:"Roboto Condensed",Arial,sans-serif;}
  .dieline{position:absolute;left:0;top:0;width:1200px;height:1200px;}
  .dieline .panel{fill:url(#panel-fill);}

  .label{position:absolute;overflow:hidden;background:var(--blue);}
  .label.is-inverted{transform:rotate(180deg);}
  .label-wave{position:absolute;left:0;top:0;width:100%;height:100%;}
  .label-wave .cream{fill:var(--cream);}
  .label-wave .edge{fill:none;stroke:var(--gold);stroke-width:6;}

  .brand{position:absolute;left:0;right:0;top:10%;text-align:center;color:var(--logo-blue);font-weight:700;line-height:1;}
  .brand-name{display:block;font-size:40px;letter-spacing:.5px;}
  .brand-suffix{display:block;font-size:13px;letter-spacing:1.5px;margin-top:3px;}

  .services{position:absolute;left:3%;width:68%;bottom:6%;text-align:center;line-height:1.3;}
  .services-line{display:block;color:var(--yellow);font-size:14px;}
  .web{display:block;color:var(--white);font-size:12.5px;font-weight:700;}

  .product-photo{position:absolute;right:4%;bottom:7%;width:84px;height:84px;border-radius:50%;
    border:4px solid var(--gold);box-sizing:border-box;
    background:radial-gradient(circle at 40% 35%,var(--steel-a),var(--steel-b));}

  .front{left:441px;top:495px;width:316px;height:200px;}
  .side-left{left:178px;top:495px;width:263px;height:200px;}
  .side-right{left:757px;top:495px;width:263px;height:200px;}
  .lid-back{left:441px;top:45px;width:316px;height:192px;}
  .base-back{left:441px;top:960px;width:316px;height:190px;}
</style>
</head>
<body>
<main class="canvas">
  <svg class="dieline" viewBox="0 0 1200 1200" role="img" aria-label="Box dieline panels covered in a blue washer ring pattern">
    <defs>
      <linearGradient id="panel-fill" x1="0" y1="0" x2="1" y2="1">
        <stop offset="0" stop-color="#0f4fae"/>
        <stop offset="1" stop-color="#1a5fb4"/>
      </linearGradient>
    </defs>
    <path class="panel lid-ear" d="M441,45 L441,237 L215,237 Q190,237 190,212 L190,150 C190,80 300,45 441,45 Z"/>
    <path class="panel lid-ear" d="M757,45 C860,45 905,90 905,150 L905,212 Q905,237 880,237 L757,237 Z"/>
    <rect class="panel body-column" x="441" y="45" width="316" height="1105"/>
    <path class="panel side-flap" d="M178,795 V495 H190 V338 H280 L292,326 H345 L352,338 H430 V495 H441 V795 Z"/>
    <path class="panel side-flap" d="M1020,795 V495 H1010 V338 H918 L906,326 H853 L846,338 H768 V495 H757 V795 Z"/>
    <rect class="panel base-row" x="178" y="960" width="842" height="190"/>
  </svg>

  <section class="label lid-back is-inverted">
    <svg class="label-wave" viewBox="0 0 316 192" preserveAspectRatio="none" aria-hidden="true">
      <path class="cream" d="M0,0 H316 V78 C230,92 90,100 0,122 Z"/>
      <path class="edge" d="M316,78 C230,92 90,100 0,122"/>
    </svg>
    <div class="brand"><span class="brand-name">Brandell</span><span class="brand-suffix">LIMITED</span></div>
    <div class="services">
      <span class="services-line">WASHERS • STAMPINGS</span>
      <span class="services-line">ASSEMBLIES • BEARINGS</span>
      <span class="web">www.brandellgroup-ltd.com</span>
    </div>
    <div class="product-photo" role="img" aria-label="Photo of steel washers"></div>
  </section>

  <section class="label side-left">
    <svg class="label-wave" viewBox="0 0 263 200" preserveAspectRatio="none" aria-hidden="true">
      <path class="cream" d="M0,0 H263 V80 C190,95 80,110 0,132 Z"/>
      <path class="edge" d="M263,80 C190,95 80,110 0,132"/>
    </svg>
    <div class="brand"><span class="brand-name">Brandell</span><span class="brand-suffix">LIMITED</span></div>
    <div class="services">
      <span class="services-line">WASHERS • STAMPINGS</span>
      <span class="services-line">ASSEMBLIES • BEARINGS</span>
      <span class="web">www.brandellgroup-ltd.com</span>
    </div>
    <div class="product-photo" role="img" aria-label="Photo of steel washers"></div>
  </section>

  <section class="label front">
    <svg class="label-wave" viewBox="0 0 316 200" preserveAspectRatio="none" aria-hidden="true">
      <path class="cream" d="M0,0 H316 V78 C230,92 90,104 0,128 Z"/>
      <path class="edge" d="M316,78 C230,92 90,104 0,128"/>
    </svg>
    <div class="brand"><span class="brand-name">Brandell</span><span class="brand-suffix">LIMITED</span></div>
    <div class="services">
      <span class="services-line">WASHERS • STAMPINGS</span>
      <span class="services-line">ASSEMBLIES • BEARINGS</span>
      <span class="web">www.brandellgroup-ltd.com</span>
    </div>
    <div class="product-photo" role="img" aria-label="Photo of steel washers"></div>
  </section>

  <section class="label side-right">
    <svg class="label-wave" viewBox="0 0 263 200" preserveAspectRatio="none" aria-hidden="true">
      <path class="cream" d="M0,0 H263 V80 C190,95 80,110 0,132 Z"/>
      <path class="edge" d="M263,80 C190,95 80,110 0,132"/>
    </svg>
    <div class="brand"><span class="brand-name">Brandell</span><span class="brand-suffix">LIMITED</span></div>
    <div class="services">
      <span class="services-line">WASHERS • STAMPINGS</span>
      <span class="services-line">ASSEMBLIES • BEARINGS</span>
      <span class="web">www.brandellgroup-ltd.com</span>
    </div>
    <div class="product-photo" role="img" aria-label="Photo of steel washers"></div>
  </section>

  <section class="label base-back is-inverted">
    <svg class="label-wave" viewBox="0 0 316 190" preserveAspectRatio="none" aria-hidden="true">
      <path class="cream" d="M0,0 H316 V78 C230,92 90,100 0,122 Z"/>
      <path class="edge" d="M316,78 C230,92 90,100 0,122"/>
    </svg>
    <div class="brand"><span class="brand-name">Brandell</span><span class="brand-suffix">LIMITED</span></div>
    <div class="services">
      <span class="services-line">WASHERS • STAMPINGS</span>
      <span class="services-line">ASSEMBLIES • BEARINGS</span>
      <span class="web">www.brandellgroup-ltd.com</span>
    </div>
    <div class="product-photo" role="img" aria-label="Photo of steel washers"></div>
  </section>
</main>
</body>
</html>
```